High-End Print/Digital Ad for Unique Luxury Travel Company Required

Objective:
Design a compelling and visually striking advertisement that highlights our company’s unmatched luxury travel experiences. The ad should elevate our brand image, spark curiosity, and drive prospective clients to contact us.
Target Audience:
• Affluent individuals seeking extraordinary, tailor-made travel experiences
• Affluent, luxury, high-net-worth individuals looking for value, expertise, and white-glove service
• Professionals or retirees who appreciate unique, thoughtfully curated travel over mainstream tourism
Key Messages to Communicate:
• One-of-a-kind luxury travel: Once-in-a-lifetime experiences that are curated with creativity and meticulous attention to detail
• Exceptional service: White-glove, personalized planning from start to finish
• 38 years’ travel experience – expert knowledge of destinations, modes of travel, premium accommodations and well-established, meaningful industry connections.
• Highly trusted: Cruise line executives often say, “No one does what you do.”
Tone and Style:
• Elegant, luxurious, sophisticated
• Eye-catching, polished, and modern
• Professional but warm—conveys trust and credibility
• High-impact visuals (full-bleed imagery, custom graphics, or high-end photography)
Deliverables:
• One full-page print ad and digital ad
• Ready-to-print, high-resolution file + working file (PSD, AI, etc.)
Optional: Social media-optimized version or short motion-graphic variation (if designer offers it)
Inspiration & Visual Style Suggestions:
• Think Velvet Voyager, Brimley Hart Wanderer, Seven Lanterns, or Oriel Retreats ad styles
• Large, emotive imagery with elegant typography
• Clean layout that speaks luxury, clarity, and trust
Copy Direction (draft):
For those who’ve explored the world—and crave something beyond the ordinary.
Each journey is a masterfully curated experience, rich in detail, seamless in execution, and unforgettable in every way.
Founded in 1997, Tidewell Journeys is a unique travel company specializing in cruising, all-inclusive luxury properties, and tours world-wide for individuals, groups, and incentives.
We offer an exceptional range of services designed to ensure every journey is flawlessly executed and truly unforgettable.
Let us help you plan your next extraordinary adventure.
Note: You may refine the copy slightly based on layout or format needs.
Other Resources for References:
1. Website - www.tidewelljourneys.example

```html
<!DOCTYPE html>
<html lang="en">
<head>
<meta charset="utf-8">
<title>Tidewell Journeys – Full-Page Ad</title>
<link rel="stylesheet" href="https://fonts.googleapis.com/css2?family=Cinzel:wght@600;700;800&family=Figtree:wght@400;500&display=swap">
<style>
  :root {
    --stage: #cdc9c5;
    --ink: #111111;
    --white: #ffffff;
    --amber: #e38a2a;
    --sky-top: #e8a54e;
    --sky-mid: #f5c679;
    --sea-glow: #f3d9ab;
    --shore: #b9b3b4;
    --lagoon: #2e8797;
    --lagoon-deep: #1f6f82;
  }
  * { margin: 0; padding: 0; box-sizing: border-box; }
  html, body {
    width: 774px;
    height: 1200px;
    overflow: hidden;
    background: var(--stage);
  }
  .ad {
    position: absolute;
    left: 0;
    top: 99px;
    width: 774px;
    height: 1001px;
    overflow: hidden;
    font-family: "Figtree", Arial, sans-serif;
  }
  .ad__scene {
    position: absolute;
    inset: 0;
    background:
      linear-gradient(160deg, rgba(0,0,0,0) 55%, rgba(47,135,151,0.85) 80%, var(--lagoon-deep) 100%),
      linear-gradient(to bottom, var(--sky-top) 0%, var(--sky-mid) 28%, var(--sea-glow) 55%, var(--shore) 78%, #a98fae 100%);
  }
  .headline {
    position: absolute;
    right: 52px;
    top: 50px;
    font-family: "Cinzel", Georgia, serif;
    font-weight: 800;
    font-size: 46px;
    line-height: 47px;
    text-align: right;
    color: var(--ink);
  }
  .intro {
    position: absolute;
    right: 52px;
    top: 339px;
    font-size: 19.5px;
    line-height: 22.5px;
    text-align: right;
    color: var(--ink);
  }
  .founded {
    position: absolute;
    left: 0;
    top: 469px;
    width: 351px;
    height: 172px;
    background: var(--amber);
    padding: 18px 30px 0 51px;
    color: var(--white);
  }
  .founded__title {
    font-family: "Cinzel", Georgia, serif;
    font-weight: 700;
    font-size: 27px;
    line-height: 30px;
  }
  .founded__body {
    font-size: 15.5px;
    line-height: 20.5px;
  }
  .services {
    position: absolute;
    left: 51px;
    top: 753px;
    font-size: 17px;
    line-height: 20.5px;
    color: var(--white);
  }
  .cta {
    position: absolute;
    left: 507px;
    top: 801px;
    color: var(--white);
  }
  .cta__line {
    font-family: "Cinzel", Georgia, serif;
    font-weight: 700;
    font-size: 22px;
    line-height: 24.5px;
  }
  .cta__url {
    margin-top: 14px;
    font-family: "Cinzel", Georgia, serif;
    font-weight: 600;
    font-size: 13px;
    letter-spacing: 0.2px;
  }
</style>
</head>
<body>
  <main class="ad">
    <div class="ad__scene" role="img" aria-label="Aerial view of a calm bay at sunset: golden sky, a wooded headland, two small boats, a pale sandy beach with rocks and turquoise water"></div>

    <h1 class="headline">For those who’ve<br>explored<br>the world and<br>crave something<br>beyond the<br>ordinary.</h1>

    <p class="intro">Each journey is a masterfully curated<br>experience, rich in detail, seamless<br>in execution, and unforgettable in every way.</p>

    <section class="founded">
      <h2 class="founded__title">Founded in 1997,</h2>
      <p class="founded__body">Tidewell Journeys is a unique travel<br>company specializing in cruising,<br>all-inclusive luxury properties, and<br>tours world-wide for individuals,<br>groups, and incentives.</p>
    </section>

    <p class="services">We offer an<br>exceptional range of<br>services designed to<br>ensure every journey<br>is flawlessly executed and<br>truly unforgettable.</p>

    <section class="cta">
      <p class="cta__line">Let us<br>help you plan<br>your next<br>extraordinary<br>adventure.</p>
      <p class="cta__url">www.tidewelljourneys.example</p>
    </section>
  </main>
</body>
</html>
```